Store Front Window Design

We have a beautiful corner store front dental practice with no window signage. Crazy I know...that's why we need your help.

The final design will be done in all vinyl unless unless you suggest a different medium (meaning we are open to some design idea like using frosted glass, etc...).

The windows provide a lot of natural light so the design needs to keep a lot of natural light coming into the office. Keep in mind vinyl is not opaque so keep the signage aesthetically pleasing and a minimalist design to allow as much natural light in as possible. The design should follow the aesthetic from our logo. or tie into at least. We want a cohesive brand aesthetic.

I submitted some general layout ideas. There is a blue banner with advertising words which we want to be used in the final version. Even though the lettering is black, in reality the letters will be a white vinyl on the outside of the window. When you submit your work, be sure to add any special instructions (aka tell me the vision for the letters is white not black, maybe gold leaf, or forested glass...stuff like that). AND YOU DO NOT HAVE TO FOLLOW MY PATTERN! YOU ARE ARTISTS AND WE ARE LOOKING FOR AN ARTISTIC EYE CATCHING PRESENTATION OF THIS INFORMATION. MAKE IT FLASHY AND ADD SOME AESTHETIC FROM THE TOOTH LOGO.

The store front is 6 windows roughly 60'' x 36'' The smaller windows below are 27'' x 36''. Around the corner there are 3 windows. they are 60'' x 27'' lower windows are 27" x 27". We would like to keep the bottom windows clear and keep the signage on the top windows, however, we are flexible.

The front 6 windows need to have this information worked into the design.

Practice name: Vesk and Ormond Dental & Orthodontics.
Phone numbers: Marisol Vesk DDS: 415.772.0183
Tobias Ormond DDS:415.509.2371

Expertise: Dr. Vesk General Dentistry & Orthodontics
Dr. Ormond Oral Surgery & Sedation

Address: 1937 Birchwood Ave

A banner across the bottom of the top windows with some key advertisement words: "Clarivet" "Braces" "Implants" "Whiting" "Call today" "Free Consultation" "Oral Surgery" "Sedation". We like the two color idea. Its up to you to decide on the color combo. I used a Dark and light blue, but maybe a Blue and grey would nice to tire in the logo colors?

I have made some mock ideas to get the ball rolling but you do not have to stick to these designs at all, just as long as all the required information is there. Be creative with the layouts, fonts, color scheme, (just remember these are going on windows not necessarily a white background), and graphics/artistic flare (refer to logo for layout inspiration and use the logo as an actual graphic). We are running a miltimillion dollar dental practice so we want these windows to be eye catching to pull in patients and look like a million dollar design. Also all 6 windows dont need ot be used. I am really looking for creative design marketing.

The corner 3 windows need the following information: name, expertise, phone number, banner.

Dr. Vesk, General Dentistry & Orthodontics, 415.772.0183
Dr. Ormond, Oral Surgery & Sedation, 415.509.2371

There is also a front door that needs to be designed. The door is 60'' x 36'' (standard door size) We want simple white vinyl on the outside of the door. We need you to organize the information on the door, pick a easy to read font, maybe use the logo and use some of the front window signage aesthetic? Its up to you...but we we were initially thinking of just making the litters white and keep it simple but again you are the designers.

Practice name: Vesk and Ormond General Dentistry & Orthodontics

Address: 1937 Birchwood Ave

Phone numbers: Dr. Vesk 415.772.0183
Dr. Ormond 415.509.2371

Hours of operation: Mon: call for an appointment
Tues-Thurs: 9am-5pm
Sat: call for an appointment
Sun: Closed

A line saying we speak Spanish: Se Habla Espanol

*****************************************************************************************************
here are some design that we liked and some rough sketches I made to start the ball rolling. Keep in mind that there are 9 windows for the front because its a corner office, but not all of them have to have stuff on it. We want simple, streamline, classy high commanding price point aesthetic. I am hiring you for your artistic minds.

Target Market(s)

anyone who has dental needs

Industry/Entity Type

Dental

Font styles to use
Serif
Sans Serif

Colors

Designer to choose colors to be used in the design.

Requirements
Must have
• 1. The required information (see project description)
• 2. Logo
• 3. Advertisement banner running along the bottom of all 9 windows (6 in front and 3 on the side)
• NOTE: Look at pictures of the store to get a sense of the customers point of view and also as a reference to how your design will be broken up across several windows or maybe you design something special for every window. But we want the banner to run along all the windows to lead customs to the door on the side. Finally the letters will be done in white vinyl unless state otherwise, remember the window needs to let in natural light so the entire window can not be covered in vinyl.
Nice to have
• artistic flare yet simple and sleep and expensive looking aesthetic. work logo into the design.
Should not have
• The goal is to catch someone eye and give them important information about the practice.
• It should not just be words.
• It should not have to many words
• It must be readable font for cards driving by.

```html
<!DOCTYPE html>
<html lang="en">
<head>
<meta charset="utf-8">
<title>Vesk and Ormond — Storefront Window Signage</title>
<link rel="stylesheet" href="https://fonts.googleapis.com/css2?family=Montserrat:wght@600;700&family=Oswald:wght@600&display=swap">
<style>
  :root {
    --teal-deep: #1a6375;
    --teal-light: #4a9aa6;
    --charcoal: #333333;
    --white: #ffffff;
    --mullion: #bdbdbd;
    --mullion-dark: #5a5a5a;
  }
  * { margin: 0; padding: 0; box-sizing: border-box; }
  html, body { width: 1200px; height: 1200px; overflow: hidden; background: var(--white); }
  .canvas { position: relative; width: 1200px; height: 1200px; font-family: "Montserrat", sans-serif; }

  .window-row { position: absolute; left: 0; width: 1200px; height: 408px; }
  .window-row--day { top: 0; background: var(--white); }
  .window-row--night { top: 715px; background: var(--charcoal); }

  .mullion { position: absolute; top: 0; width: 1px; height: 100%; background: var(--mullion); }
  .window-row--night .mullion { background: var(--mullion-dark); }

  .doctor { position: absolute; text-align: center; width: 238px; }
  .doctor--left { left: 0; }
  .doctor--right { left: 723px; width: 242px; }
  .doctor__name {
    position: absolute; top: 143px; width: 100%;
    font-weight: 700; font-size: 27px; line-height: 29px; letter-spacing: 0.5px;
    color: var(--teal-light);
  }
  .doctor__phone {
    position: absolute; top: 292px; width: 100%;
    font-weight: 700; font-size: 34px; line-height: 42px; letter-spacing: 2px;
    color: var(--teal-deep);
  }
  .doctor__phone .phone-icon { width: 30px; height: 30px; vertical-align: -3px; margin-right: 2px; }

  .split { position: absolute; left: 0; width: 1200px; display: flex; }
  .split__left { width: 482px; text-align: right; padding-right: 3px; }
  .split__right { flex: 1; text-align: left; padding-left: 3px; }

  .specialties { top: 34px; font-weight: 700; font-size: 38px; line-height: 42px; color: var(--teal-deep); letter-spacing: 0.5px; }
  .specialties .row { display: flex; width: 100%; }
  .address-number { top: 236px; font-weight: 700; font-size: 36px; letter-spacing: 12px; color: var(--teal-light); }
  .address-street { top: 296px; font-weight: 700; font-size: 30px; letter-spacing: 1.5px; color: var(--teal-light); }
  .address-number .split__right, .address-street .split__right { padding-left: 9px; }
  .address-number .split__left { padding-right: 0; }

  .window-row--night .doctor__name,
  .window-row--night .doctor__phone,
  .window-row--night .specialties,
  .window-row--night .address-number,
  .window-row--night .address-street { color: var(--white); }

  .service-band {
    position: absolute; left: 0; width: 1200px; height: 74px;
    display: flex; align-items: center;
    font-family: "Oswald", sans-serif; font-weight: 600; font-size: 30px; letter-spacing: 3.5px;
  }
  .service-band--teal { top: 408px; background: var(--teal-deep); color: var(--white); }
  .service-band--plain { top: 1123px; height: 77px; background: var(--white); color: var(--charcoal); }
  .service-band span { position: absolute; transform: translateX(-50%); white-space: nowrap; }
</style>
</head>
<body>
<div class="canvas">

  <section class="window-row window-row--day">
    <div class="mullion" style="left:238px"></div>
    <div class="mullion" style="left:480px"></div>
    <div class="mullion" style="left:723px"></div>
    <div class="mullion" style="left:965px"></div>

    <div class="specialties split" style="flex-direction:column">
      <div class="row"><span class="split__left">GENRAL</span><span class="split__right">DENTISTRY</span></div>
      <div class="row"><span class="split__left">ORTHO</span><span class="split__right">DONTICS</span></div>
      <div class="row"><span class="split__left">SED</span><span class="split__right">ATION</span></div>
    </div>
    <div class="address-number split"><span class="split__left">1 9</span><span class="split__right">3 7</span></div>
    <div class="address-street split"><span class="split__left">BIRCHWOOD</span><span class="split__right">AVENUE</span></div>

    <div class="doctor doctor--left">
      <p class="doctor__name">MARISOL<br>VESK<br>D.D.S.</p>
      <p class="doctor__phone"><svg class="phone-icon" viewBox="0 0 30 30"><circle cx="15" cy="15" r="13" fill="none" stroke="currentColor" stroke-width="2"/><path d="M12 8c-2 1-3 3-3 6s2 7 5 8c1 0 2-1 2-2l-2-3-2 1c-1-2-1-4 0-6l2 0 1-3-1-1z" fill="currentColor"/></svg>(415)<br>772-0183</p>
    </div>
    <div class="doctor doctor--right">
      <p class="doctor__name">TOBIAS<br>ORMOND<br>D.D.S.</p>
      <p class="doctor__phone"><svg class="phone-icon" viewBox="0 0 30 30"><circle cx="15" cy="15" r="13" fill="none" stroke="currentColor" stroke-width="2"/><path d="M12 8c-2 1-3 3-3 6s2 7 5 8c1 0 2-1 2-2l-2-3-2 1c-1-2-1-4 0-6l2 0 1-3-1-1z" fill="currentColor"/></svg>(415)<br>509-2371</p>
    </div>
  </section>

  <nav class="service-band service-band--teal">
    <span style="left:117px">CLARIVET</span>
    <span style="left:358px">BRACES</span>
    <span style="left:602px">IMPLANTS</span>
    <span style="left:844px">WHITENING</span>
    <span style="left:1082px">ORAL SUGARY</span>
  </nav>

  <section class="window-row window-row--night">
    <div class="mullion" style="left:239px"></div>
    <div class="mullion" style="left:480px"></div>
    <div class="mullion" style="left:722px"></div>
    <div class="mullion" style="left:963px"></div>

    <div class="specialties split" style="flex-direction:column">
      <div class="row"><span class="split__left">GENRAL</span><span class="split__right">DENTISTRY</span></div>
      <div class="row"><span class="split__left">ORTHO</span><span class="split__right">DONTICS</span></div>
      <div class="row"><span class="split__left">SED</span><span class="split__right">ATION</span></div>
    </div>
    <div class="address-number split"><span class="split__left">1 9</span><span class="split__right">3 7</span></div>
    <div class="address-street split"><span class="split__left">BIRCHWOOD</span><span class="split__right">AVENUE</span></div>

    <div class="doctor doctor--left">
      <p class="doctor__name">MARISOL<br>VESK<br>D.D.S.</p>
      <p class="doctor__phone"><svg class="phone-icon" viewBox="0 0 30 30"><circle cx="15" cy="15" r="13" fill="none" stroke="currentColor" stroke-width="2"/><path d="M12 8c-2 1-3 3-3 6s2 7 5 8c1 0 2-1 2-2l-2-3-2 1c-1-2-1-4 0-6l2 0 1-3-1-1z" fill="currentColor"/></svg>(415)<br>772-0183</p>
    </div>
    <div class="doctor doctor--right">
      <p class="doctor__name">TOBIAS<br>ORMOND<br>D.D.S.</p>
      <p class="doctor__phone"><svg class="phone-icon" viewBox="0 0 30 30"><circle cx="15" cy="15" r="13" fill="none" stroke="currentColor" stroke-width="2"/><path d="M12 8c-2 1-3 3-3 6s2 7 5 8c1 0 2-1 2-2l-2-3-2 1c-1-2-1-4 0-6l2 0 1-3-1-1z" fill="currentColor"/></svg>(415)<br>509-2371</p>
    </div>
  </section>

  <nav class="service-band service-band--plain">
    <span style="left:118px">CLARIVET</span>
    <span style="left:359px">BRACES</span>
    <span style="left:602px">IMPLANTS</span>
    <span style="left:843px">WHITENING</span>
    <span style="left:1079px">ORAL SUGARY</span>
  </nav>

</div>
</body>
</html>
```